Dorrie's Letterhead

Letterhead should say: Dorrie Fenwick Childern's Book Author/Illustrator

Font should be fun and colorful, but not so distracting that it over shadows the letters content. My business card is shaped like a bone so I would like to keep that shape somewhere in the theme of the letterhead. You can find my book on Bookvale Wiggo and the Silver Kite if you would like to get a sense of my artistic style.
Updates

While I did say I want to carry out the bone theme. Don't be afraid to expand on that example: book shaped like a bone, paint brush...really go for it.

Surprise me! Good luck

Target Market(s)

Adults buying my book

Industry/Entity Type

Business

Requirements
Must have
• Fun colorful
Should not have
• Only one color

```html
<!DOCTYPE html>
<html lang="en">
<head>
<meta charset="utf-8">
<title>Dorrie Fenwick Letterhead</title>
<link href="https://fonts.googleapis.com/css2?family=Open+Sans:wght@400;600;700;800&family=Raleway:wght@400;500&display=swap" rel="stylesheet">
<style>
  :root {
    --backdrop: #e4e4e4;
    --paper-edge: #f4f5f5;
    --paper: #cfe0e6;
    --corner-tint: #eef2f3;
    --ink: #2f3336;
    --ink-soft: #4a4f53;
    --brand: #3f7fc2;
    --tagline: #e58a3a;
    --doodle-red: #e0475a;
    --doodle-pink: #d88bb6;
    --doodle-purple: #b67ad0;
    --doodle-green: #8cc06a;
    --doodle-blue: #6fb3d8;
    --doodle-teal: #5fc2c6;
    --stem: #a9b8bf;
  }
  * { box-sizing: border-box; margin: 0; padding: 0; }
  html, body { width: 1200px; height: 1000px; overflow: hidden; background: var(--backdrop); }
  .letterhead {
    position: absolute; left: 270px; top: 33px; width: 660px; height: 934px;
    background: var(--paper-edge); padding: 16px;
    box-shadow: 0 2px 10px rgba(0,0,0,0.08);
  }
  .sheet {
    position: relative; width: 100%; height: 100%; background: var(--paper);
    overflow: hidden; font-family: "Open Sans", sans-serif; color: var(--ink);
  }
  .corner-art {
    position: absolute; left: 0; top: 0; width: 170px; height: 180px;
    background: radial-gradient(ellipse at 0 0, var(--corner-tint) 0%, var(--corner-tint) 55%, rgba(238,242,243,0) 72%);
  }
  .brand { position: absolute; right: 30px; top: 34px; text-align: left; }
  .brand-name {
    font-family: "Open Sans", sans-serif; font-weight: 800; font-size: 25px;
    color: var(--brand); letter-spacing: 0.3px; line-height: 1;
  }
  .brand-tagline {
    font-family: "Open Sans", sans-serif; font-weight: 600; font-size: 11.5px;
    color: var(--tagline); margin-top: 3px; letter-spacing: 0.2px;
  }
  .recipient { position: absolute; left: 38px; top: 232px; font-size: 11px; line-height: 1.35; color: var(--ink-soft); font-style: normal; }
  .recipient strong { color: var(--ink); font-weight: 700; }
  .letter-body { position: absolute; left: 38px; top: 300px; width: 560px; font-size: 11px; line-height: 1.55; }
  .letter-body p { margin-bottom: 11px; }
  .sign-off { position: absolute; left: 38px; top: 672px; }
  .signature { width: 110px; height: 26px; border-radius: 13px; background: linear-gradient(90deg, rgba(47,51,54,0.55), rgba(47,51,54,0.25)); }
  .sign-name { font-size: 9px; margin-top: 6px; color: var(--ink); }
  .doodles { position: absolute; left: 0; top: 0; width: 100%; height: 100%; pointer-events: none; }
  .contact { position: absolute; font-family: "Raleway", sans-serif; font-size: 12px; color: var(--ink-soft); font-weight: 500; white-space: nowrap; }
  .contact-cell { left: 228px; top: 846px; }
  .contact-email { left: 380px; top: 812px; }
</style>
</head>
<body>
<main class="letterhead">
  <div class="sheet">
    <div class="corner-art" role="img" aria-label="Soft white cloud decoration in the top corner"></div>

    <header class="brand">
      <div class="brand-name">Dorrie Fenwick</div>
      <div class="brand-tagline">Children's book Author/Illustrator</div>
    </header>

    <address class="recipient">
      <strong>Lorem ipsum</strong><br>
      Dolor sit amet<br>
      ei eros vidit sonet<br>
      sed
    </address>

    <section class="letter-body">
      <p>Lorem ipsum dolor sit amet, ei eros vidit sonet eum, sed ea aliquam offendit. Reque quando labitur nec in, no solum ceteros est. Accumsan pertinacia an qui. Te vidisse recteque pro, cu per habemus officiis, eos ex mutat possim ornatus. Appetere principes eloquentiam vis ei, an mea alia petentium dignissim, te justo omnium duo.</p>
      <p>Movet laoreet delicatissimi cum id. Essent dissentiet cu cum, atqui augue iriure qui ea. Liber propriae et sed. Euismod ornatus scaevola et pro.</p>
      <p>Verterem interesset disputationi vim et, laudem persecuti quo eu. Mea viderer vulputate ut. Ad scripta scaevola appetere usu, omnium forensibus sed cu, dolorum admodum postulant mea et. Eos ut ubique graeco insolens, etiam electram assentior cum at.</p>
      <p>In eos solum verterem facilisis, magna scaevola explicari has ex, at vidisse percipitur cum. At dicam postea luptatum sea, sed te timeam principes disputando, postea scaevola eloquentiam quo eu. Cetero concludaturque cu ius, nam erat detraxit ut, in his cetero vocent erroribus. Eu sint nulla comprehensam qui. Dolor dolorum splendide ei est, id usu inani liber deterruisset.</p>
      <p>Omnis intellegat intellegam duo cu, no ornatus partiendo referrentur has</p>
    </section>

    <div class="sign-off">
      <div class="signature" role="img" aria-label="Handwritten signature of Dorrie Fenwick"></div>
      <div class="sign-name">Dorrie Fenwick, Children's book Author/Illustrator</div>
    </div>

    <svg class="doodles" viewBox="0 0 628 902">
      <g fill="none" stroke="var(--stem)" stroke-width="1">
        <path d="M232 764 C270 800 330 810 380 790 C410 778 420 760 420 730"/>
        <path d="M420 730 C450 690 520 660 560 640"/>
      </g>
      <circle cx="232" cy="756" r="16" fill="var(--doodle-red)" opacity="0.55" role="img" aria-label="Butterfly doodle"/>
      <circle cx="325" cy="690" r="11" fill="var(--doodle-pink)" opacity="0.5" role="img" aria-label="Flower doodle"/>
      <circle cx="420" cy="708" r="16" fill="var(--doodle-purple)" opacity="0.45" role="img" aria-label="Little chick doodle"/>
      <circle cx="560" cy="632" r="13" fill="var(--doodle-teal)" opacity="0.45" role="img" aria-label="Bird doodle"/>
      <circle cx="580" cy="700" r="11" fill="var(--doodle-green)" opacity="0.5" role="img" aria-label="Flower doodle"/>
      <circle cx="66" cy="786" r="12" fill="var(--doodle-green)" opacity="0.5" role="img" aria-label="Flower doodle"/>
      <circle cx="142" cy="840" r="12" fill="var(--doodle-blue)" opacity="0.5" role="img" aria-label="Little chick doodle"/>
    </svg>

    <div class="contact contact-cell">Cell: (555) 014-2290</div>
    <div class="contact contact-email">Email: wiggoskitehouse@mailvale.net</div>
  </div>
</main>
</body>
</html>
```